Label for Whiskey and Rum Bottle

We are a distillery. Whiskey and Rum We like to have a new label for our bottles. The whiskey bottles are in a wooden case. http://www.kornfaesser.ch/store/product/talwinkel-obermatt-single-malt-whiskey-nr-6 The Rum Bottles have no package. The label is even more important. http://www.kornfaesser.ch/store/product/talwinkel-obermatter-rum You can see the form of the bottles here www.kornfaesser.ch/store Whiskey and rum bottles are for a liter (50 cl) The labels can be with a picture or without. We would like to have something completely new. Therefore we don`t like to make much prescriptions concerning the design. We don`t like to give too much information (text) on the label. Just the information required by law. Consumers should understand the labels without long-reading. (The label-text is below) The 2 labels (Whiskey and rum) should look similar. Probably they have a different color or a different picture or .... It should be clear that the 2 products are from the same distillery. We have the intention to change all our existing labels over time. This gives designers the chance for follow-up projects.

Target Market(s)

Adults, liquor lovers

Requirements
Must have
• Information on the label is in German. (See "") Whiskey: - the name of the whiskey is "Talwinkel Obermatt Single Malt Whiskey" - The Whiskey was matured 5 years in a sherry "5 years in the sherry barrel stored" - The Alcohol content is 40% volumes "40% Vol "- The bottle contents 50 cl" 5 dl "- The distillery is" Distillery Brunnacher, Tornwil, www.kornfaesser.ch "- The producer is" Kelvor GmbH "Rum: - The name is" Talwinkel Obermatter Rum "- The alcohol content is 37% Volumes "37% Vol" - The bottle contens 50 cl "5 dl" - The distillery is "Distillery Brunnacher, Tornwil, www.kornfaesser.ch" - The producer is "Kelvor GmbH"
Nice to have
• Premium looking label Only front label preferred Only necessary text on the label
Should not have
• No special print techniques necessary No special paper form

```html
<!DOCTYPE html>
<html lang="de">
<head>
<meta charset="utf-8">
<title>Talwinkel Obermatt Single Malt Whiskey – Etikett</title>
<link rel="stylesheet" href="https://fonts.googleapis.com/css2?family=UnifrakturMaguntia&family=Cormorant+Garamond:wght@500;600&display=swap">
<style>
  :root {
    --page: #ffffff;
    --label: #1e1e1e;
    --gold: #c9a84f;
    --ivory: #f4f1ea;
    --copper: #b5623a;
    --ornament-soft: rgba(255, 255, 255, 0.10);
  }
  * { margin: 0; padding: 0; box-sizing: border-box; }
  html, body {
    width: 1200px;
    height: 900px;
    overflow: hidden;
    background: var(--page);
  }
  .label {
    position: absolute;
    left: 300px;
    top: 50px;
    width: 601px;
    height: 800px;
    background: var(--label);
    color: var(--ivory);
    font-family: "Cormorant Garamond", Georgia, serif;
  }
  .crest-ornament {
    position: absolute;
    left: 61px;
    top: 70px;
    width: 477px;
    height: 78px;
    background: radial-gradient(ellipse at 50% 70%, var(--ornament-soft), transparent 70%);
  }
  .product-name {
    position: absolute;
    left: 0;
    right: 0;
    top: 160px;
    text-align: center;
    font-family: "UnifrakturMaguntia", "Times New Roman", serif;
    font-size: 50px;
    line-height: 1;
    color: var(--gold);
  }
  .product-type {
    position: absolute;
    left: 0;
    right: 0;
    top: 233px;
    text-align: center;
    font-size: 24px;
    font-weight: 500;
    letter-spacing: 0.32em;
    padding-left: 0.32em;
    line-height: 1;
    color: var(--gold);
  }
  .divider-ornament {
    position: absolute;
    left: 67px;
    top: 264px;
    width: 466px;
    height: 20px;
    background: linear-gradient(90deg, transparent, var(--ornament-soft) 15%, rgba(255,255,255,0.18) 50%, var(--ornament-soft) 85%, transparent);
  }
  .maturation {
    position: absolute;
    left: 0;
    right: 0;
    top: 311px;
    text-align: center;
    font-size: 18px;
    font-weight: 600;
    letter-spacing: 0.2em;
    padding-left: 0.2em;
    color: var(--gold);
  }
  .distillery-mark {
    position: absolute;
    left: 0;
    right: 0;
    top: 600px;
    text-align: center;
  }
  .distillery-mark .dot {
    display: block;
    width: 34px;
    height: 34px;
    margin: 0 auto 26px;
    border-radius: 50%;
    background: var(--copper);
  }
  .distillery-mark .name {
    font-size: 24px;
    font-weight: 500;
    line-height: 1.02;
    letter-spacing: 0.04em;
    text-transform: uppercase;
    color: var(--ivory);
  }
  .producer {
    position: absolute;
    left: 0;
    right: 0;
    top: 722px;
    text-align: center;
    font-size: 14.5px;
    font-weight: 500;
    line-height: 18px;
    letter-spacing: 0.12em;
    color: var(--ivory);
  }
  .volume-info {
    position: absolute;
    top: 740px;
    font-size: 18px;
    font-weight: 500;
    color: var(--ivory);
  }
  .volume-info.alcohol { left: 33px; }
  .volume-info.content { right: 40px; }
</style>
</head>
<body>
  <main class="label">
    <div class="crest-ornament" role="img" aria-label="Feines weisses Zierornament mit Krone über dem Produktnamen"></div>
    <h1 class="product-name">Talwinkel Obermatt</h1>
    <p class="product-type">SINGLE MALT WHISKEY</p>
    <div class="divider-ornament" role="img" aria-label="Weisse Zierlinie mit Schnörkel in der Mitte"></div>
    <p class="maturation">5 Jahre im Sherry Fass gelagert</p>

    <div class="distillery-mark">
      <span class="dot"></span>
      <p class="name">Brennerei<br>Brunnacher</p>
    </div>

    <p class="producer">
      Brennerei Brunnacher, Tornwil<br>
      www.kornfaesser.ch<br>
      Kelvor GmbH
    </p>

    <p class="volume-info alcohol">40% Vol</p>
    <p class="volume-info content">50 cl</p>
  </main>
</body>
</html>
```